Geschäftspapiere für Beratungsleistung
Zielgruppe
DieKlarwerkstatt.com ist eine Beratungsleistung der Voltrin Consulting GmbH.
Wir beraten kleine und mittlere Unternehmen (B2B) in Fragen des Datenschutz. Wir unterstützen unsere Kunden dabei, die notwendigen Richtlinien, Dokumentationen und Prozesse einzuführen, die sicherstellen, dass unsere Kunden die gesetzlichen Vorgaben zum Schutz personenbezogener Daten einhalten.
Aufgabenstellung
Wichtiger Hinweis: Wir möchten die Gestaltung von Briefpapier und Visitenkarten beauftragen. Da grafikfinder.de das nicht als Standardprojekt mit entsprechender Preisskala vorsieht, haben wir einen individuellen Preis festgelegt (160 Euro Briefbogen + 120 Euro Visitenkarten).
'Die Klarwerkstatt' ist eine Marke der Voltrin Consulting GmbH. Das Markenlogo ist bereits vorhanden.
Die Aufgabenstellung ist es, einen Briefbogen mit den Geschäftsangaben, sowie einen Folgebogen ohne Geschäftsangaben zu entwickeln. Außerdem sollen Visitenkarten entworfen werden.
Die Geschäftspapiere sollen sich in der Gestaltung an die Website von 'Die Klarwerkstatt' anlehnen. Da die Website noch nicht live sind, ist der Entwurf der Homepage angehängt. Wichtig: die im Banner verwendete Teaser-Grafik soll nicht als Hintergrund für die Geschäftspapiere verwendet werden.
Bitte beachten Sie, dass 'Die Klarwerkstatt' kein Unternehmen ist, sondern eine Marke der Voltrin Consulting ist. Die Angaben auf den Geschäftspapieren beziehen sich daher auf die Voltrin Consulting GmbH. Der Briefbogen der Voltrin Consulting ist angehängt. Dort können die Geschäftsangaben entnommen werden. Das Voltrin Logo soll auf den Geschäftspapieren für 'Die Klarwerkstatt' nicht verwendet werden. Der Entwurf soll auf das Logo und Erscheinungsbild von 'Die Klarwerkstatt' abgestellt werden.
Die Entwürfe möchten wir zum einen im Indesign-Format haben, um diese an einen Druckdienstleister weiterzugeben bzw. die entsprechenden pdfs nach Vorgaben der Druckerei erzeugen zu können. Den Briefbogen und den Folgebogen möchten wir außerdem im Microsoft Word-Format haben, um Geschäftsbriefe direkt aus Word heraus zu erzeugen zu können. Die Dokumente sollen dann entweder als pdf per E-Mail versendet oder auf einem Tintenstrahldrucker gedruckt werden. Das Design sollte also auch auf einem Büro-Farbtintenstrahldrucker in guter Darstellung gedruc..

```html
<!DOCTYPE html>
<html lang="de">
<head>
<meta charset="utf-8">
<title>Die Klarwerkstatt – Briefbogen</title>
<link rel="stylesheet" href="https://fonts.googleapis.com/css2?family=Exo+2:wght@300;400;700&display=swap">
<style>
  :root {
    --brand-blue: #0b4f96;
    --accent-orange: #ef7d22;
    --text-ink: #34418a;
    --paper: #ffffff;
  }
  * { margin: 0; padding: 0; box-sizing: border-box; }
  html, body { width: 927px; height: 1200px; overflow: hidden; background: var(--paper); }
  .letterhead {
    position: relative;
    width: 927px;
    height: 1200px;
    font-family: "Exo 2", sans-serif;
    font-weight: 300;
    color: var(--text-ink);
  }
  .brand {
    position: absolute;
    left: 106px;
    top: 76px;
    display: flex;
    align-items: flex-start;
    gap: 14px;
  }
  .brand-square {
    width: 17px;
    height: 17px;
    background: var(--brand-blue);
    margin-top: 6px;
  }
  .brand-name {
    font-weight: 700;
    font-size: 30px;
    line-height: 26px;
    letter-spacing: -0.3px;
    color: var(--brand-blue);
    text-transform: uppercase;
  }
  .contact {
    position: absolute;
    left: 648px;
    top: 74px;
    height: 108px;
    border-left: 1px solid var(--accent-orange);
    padding-left: 9px;
    font-size: 12.3px;
    line-height: 12.2px;
  }
  .contact p + p { margin-top: 12px; }
  .rule {
    position: absolute;
    left: 106px;
    width: 708px;
  }
  .rule-blue { height: 4px; background: var(--brand-blue); }
  .rule-orange { height: 1px; background: var(--accent-orange); }
  .header-rule-blue { top: 193px; }
  .header-rule-orange { top: 198px; }
  .footer-rule-orange { top: 1078px; left: 105px; width: 710px; }
  .footer-rule-blue { top: 1081px; left: 105px; width: 710px; }
  .footer {
    position: absolute;
    top: 1102px;
    left: 106px;
    display: flex;
    font-size: 12.3px;
    line-height: 12.2px;
  }
  .footer-col {
    border-left: 1px solid var(--accent-orange);
    padding-left: 5px;
    height: 70px;
  }
  .footer-col p + p { margin-top: 12px; }
  .footer-col.company { width: 139px; }
</style>
</head>
<body>
  <div class="letterhead">
    <div class="brand">
      <div class="brand-square"></div>
      <div class="brand-name">Die Klarwerkstatt</div>
    </div>

    <address class="contact" style="font-style: normal;">
      <p>Voltrin Consulting GmbH<br>Südliche Parkstr. 9 B<br>D-82064 Talheim</p>
      <p>Fon +49 89 552873-00<br>Fax +49 89 552873-09</p>
      <p>info@voltrin-consulting.de<br>www.voltrin-consulting.de</p>
    </address>

    <div class="rule rule-blue header-rule-blue"></div>
    <div class="rule rule-orange header-rule-orange"></div>

    <div class="rule rule-orange footer-rule-orange"></div>
    <div class="rule rule-blue footer-rule-blue"></div>

    <footer class="footer">
      <div class="footer-col company">
        <p>Geschäftsführerin:<br>Henrike Lausberg</p>
        <p>Amtsgericht München<br>HRB 318562<br>USt-ID: DE407152689</p>
      </div>
      <div class="footer-col bank">
        <p>Nordtal Bank<br>Konto: 5820417<br>BLZ: 70142236</p>
        <p>BIC: NORTDEM1TLH<br>IBAN: DE47701422360005820417</p>
      </div>
    </footer>
  </div>
</body>
</html>
```